Presentation PDF covers

Produce a PDF front cover & Back cover for PDF sales proposal - will also need to be able to print as a presentation folder if the customer requires a hard copy. The PDF & Covers will need to be A4 portrait with the image (main picture as large as possible) The company Logo to be in a corner with other logos displayed on front.

the rear cover to just have company details on back -

```html
<!DOCTYPE html>
<html lang="en">
<head>
<meta charset="utf-8">
<title>Voltmark Compliance – Proposal Covers</title>
<link href="https://fonts.googleapis.com/css2?family=Montserrat:wght@400;500;600;700&display=swap" rel="stylesheet">
<style>
  :root {
    --stage: #b9b7c2;
    --paper: #ffffff;
    --ink: #45464b;
    --band-grey: #58585c;
    --brand-yellow: #f6c400;
    --badge-grey: #d9dadf;
  }
  * { box-sizing: border-box; margin: 0; padding: 0; }
  html, body { width: 827px; height: 1200px; overflow: hidden; }
  body {
    background: var(--stage);
    font-family: "Montserrat", sans-serif;
    color: var(--ink);
    position: relative;
  }
  .cover-spread {
    position: absolute;
    left: 20px; top: 324px;
    width: 787px; height: 552px;
    background:
      linear-gradient(125deg, transparent 0 30%, rgba(0,0,0,0.025) 30% 38%, transparent 38% 55%, rgba(0,0,0,0.02) 55% 62%, transparent 62%),
      var(--paper);
    box-shadow: 0 4px 14px rgba(0,0,0,0.18);
    overflow: hidden;
  }
  .spine {
    position: absolute; left: 383px; top: 0; width: 20px; height: 100%;
    background: linear-gradient(90deg, transparent, rgba(0,0,0,0.05), transparent);
  }
  .hero-scene {
    position: absolute; left: 322px; top: 112px; width: 465px; height: 360px;
    background:
      radial-gradient(ellipse at 72% 58%, rgba(47,52,99,0.35), transparent 42%),
      radial-gradient(ellipse at 50% 42%, rgba(47,174,134,0.45), transparent 45%),
      radial-gradient(ellipse at 24% 55%, rgba(63,120,200,0.35), transparent 40%),
      linear-gradient(180deg, #ffffff 0%, #e8ecef 70%, #ffffff 100%);
    border-radius: 40px 0 0 60px;
  }
  .brand-lockup { position: absolute; width: 190px; text-align: center; }
  .brand-mark {
    display: block; margin: 0 auto 8px;
    width: 40px; height: 40px; border-radius: 50%;
    background: var(--brand-yellow);
  }
  .brand-name {
    font-weight: 700; font-size: 12px; letter-spacing: 0.05em;
    color: var(--ink); line-height: 1.1; white-space: nowrap;
  }
  .brand-name .ltd {
    display: block; font-size: 8px; letter-spacing: 0.35em;
    border-bottom: 1px solid var(--ink); padding-bottom: 1px;
  }
  .brand-tagline {
    font-size: 4.6px; letter-spacing: 0.42em; margin-top: 2px;
    font-weight: 500; white-space: nowrap;
  }
  .back-lockup { left: 101px; top: 338px; }
  .front-lockup { left: 591px; top: 26px; }
  .company-details {
    position: absolute; left: 76px; top: 432px; width: 240px;
    text-align: center; font-size: 7.6px; line-height: 1.45;
  }
  .company-details .registration { margin-top: 8px; font-weight: 600; }
  .company-details .contact { margin-top: 13px; font-weight: 700; font-size: 8px; line-height: 1.6; }
  .accreditation-row {
    position: absolute; left: 405px; top: 512px; width: 366px;
    display: flex; justify-content: space-between; align-items: center;
  }
  .badge { width: 32px; height: 14px; background: var(--badge-grey); border-radius: 2px; }
  .badge.round { width: 16px; height: 16px; border-radius: 50%; }
  .footer-band { position: absolute; left: 0; bottom: 0; width: 100%; height: 12px; }
</style>
</head>
<body>
  <main class="cover-spread">
    <div class="spine"></div>

    <section class="front-cover">
      <div class="hero-scene" role="img" aria-label="Illustration of a renewable energy setup: wind turbines, solar panels, a large green battery, an electric car charging and a house with rooftop solar panels among trees"></div>
      <div class="brand-lockup front-lockup">
        <span class="brand-mark"></span>
        <div class="brand-name">VOLTMARK COMPLIANCE<span class="ltd">LTD</span></div>
        <div class="brand-tagline">ELECTRICAL MECHANICAL RENEWABLE</div>
      </div>
      <div class="accreditation-row" aria-label="Accreditation badges">
        <span class="badge"></span>
        <span class="badge"></span>
        <span class="badge"></span>
        <span class="badge"></span>
        <span class="badge"></span>
        <span class="badge"></span>
        <span class="badge round"></span>
        <span class="badge"></span>
      </div>
    </section>

    <section class="back-cover">
      <div class="brand-lockup back-lockup">
        <span class="brand-mark"></span>
        <div class="brand-name">VOLTMARK COMPLIANCE<span class="ltd">LTD</span></div>
        <div class="brand-tagline">ELECTRICAL MECHANICAL RENEWABLE</div>
      </div>
      <div class="company-details">
        <p>Unit 4B, Harrowfield Business Park<br>Harrowfield, Ludlow<br>Shropshire, SY8 2QT</p>
        <p class="registration">Registered in England No: 10923418<br>Vat Reg No: 417 3852 06</p>
        <p class="contact">sales@voltmarkcompliance.co.uk<br>www.voltmarkcompliance.co.uk</p>
      </div>
    </section>

    <svg class="footer-band" viewBox="0 0 787 12" preserveAspectRatio="none" aria-hidden="true">
      <rect x="0" y="0" width="787" height="7" fill="var(--band-grey)"/>
      <polygon points="490,3 787,3 787,12 484,12" fill="var(--brand-yellow)"/>
    </svg>
  </main>
</body>
</html>
```